Lift Her Forward, 2019 Save The Date

Please develop a save the date flyer our 4th Annual Lift Her Forward and See Her Rise! This event is focused on maintaining participation and appreciation for women in the design and construction industry.

This unique Forum provides a venue to engage everyone from executives to those just beginning their careers with active, hands-on sessions and vibrant networking with the best and brightest in the A/E/C industry. In our usual Q-TarVM Forum style, Keynotes become table participants and table participants become presenters, encouraging participants to assimilate what they are learning. Join local, state and national leaders and subject matter experts as we candidly explore and address the issues affecting women in our industry.

Industry/Entity Type

Construction

Font styles to use
Sans Serif

Requirements
Must have
• This is a save the date, Must have:
• Q-TarVM Logo
• Title: 4th Annual Lift Her Forward and See Her Rise!
• Date: January 25, 2019
• Location: Harbor Crest Resort and Spa, San Marcos, TX
Nice to have
• A header that can easily be pulled to add to other marketing materials and for use across other platforms (web, etc.).

```html
<!DOCTYPE html>
<html lang="en">
<head>
<meta charset="utf-8">
<title>Lift Her Forward 2019 – Save the Date</title>
<link rel="stylesheet" href="https://fonts.googleapis.com/css2?family=Libre+Baskerville:wght@700&family=Questrial&display=swap">
<style>
  :root {
    --navy: #1b3a8c;
    --navy-deep: #142f78;
    --ink: #3b3b3d;
    --green: #5f8c2d;
    --green-light: #8cb83f;
    --green-dark: #66963a;
    --paper: #d6d7d9;
    --white: #ffffff;
  }
  * { margin: 0; padding: 0; box-sizing: border-box; }
  html, body { width: 848px; height: 1200px; overflow: hidden; background: var(--paper); }
  .flyer {
    position: relative;
    width: 848px;
    height: 1200px;
    overflow: hidden;
    background: var(--paper);
    font-family: "Questrial", sans-serif;
  }
  .texture {
    position: absolute;
    right: 0; top: 0;
    width: 520px; height: 680px;
    background: radial-gradient(ellipse at 85% 25%, #bfc0c3 0%, #cfd0d2 45%, rgba(214,215,217,0) 75%);
  }
  .shapes { position: absolute; inset: 0; }
  .header-brand { position: absolute; left: 0; top: 0; width: 848px; height: 200px; }
  .brand-mark {
    position: absolute;
    left: 109px; top: 54px;
    width: 121px; height: 121px;
    border-radius: 50%;
    background: var(--white);
  }
  .brand-name {
    position: absolute;
    left: 262px; top: 60px;
    font-size: 62px;
    line-height: 1;
    color: var(--white);
    white-space: nowrap;
  }
  .brand-rule {
    position: absolute;
    left: 264px; top: 129px;
    width: 268px; height: 1.5px;
    background: var(--white);
  }
  .brand-tagline {
    position: absolute;
    left: 264px; top: 138px;
    font-size: 15px;
    line-height: 1.2;
    color: var(--white);
    white-space: nowrap;
  }
  .photo {
    position: absolute;
    left: 0; top: 290px;
    width: 400px; height: 740px;
    border-radius: 0 140px 30px 0;
    background: linear-gradient(175deg, #b9a08a 0%, #6e5a4c 22%, #2e2e33 45%, #c7c8cb 58%, #bdbec1 70%, #2b2d34 82%, #24262c 100%);
  }
  .event-date {
    position: absolute;
    left: 60px; top: 706px;
    width: 330px;
    color: var(--navy);
    text-align: center;
    white-space: nowrap;
  }
  .event-date .day { font-size: 46px; line-height: 1; display: block; }
  .event-date .day sup { font-size: 26px; vertical-align: 18px; }
  .event-date .year { font-size: 64px; line-height: 1.05; display: block; }
  .title {
    position: absolute;
    right: 26px; top: 448px;
    text-align: right;
    font-family: "Libre Baskerville", serif;
    font-weight: 700;
    white-space: nowrap;
  }
  .title .edition { display: block; font-size: 80px; line-height: 1; color: var(--navy); letter-spacing: -1px; }
  .title .edition sup { font-size: 36px; vertical-align: 38px; }
  .title .lead { display: block; font-size: 29px; line-height: 1.2; color: var(--ink); margin-top: 8px; }
  .title .rise { display: block; font-size: 64px; line-height: 1.05; color: var(--green); letter-spacing: -0.5px; }
  .venue {
    position: absolute;
    left: 360px; top: 1064px;
    width: 460px;
    text-align center;
    text-align: center;
    color: var(--white);
    font-size: 33px;
    line-height: 1.22;
    white-space: nowrap;
  }
</style>
</head>
<body>
<main class="flyer">
  <div class="texture" role="img" aria-label="Soft grey diamond texture"></div>

  <svg class="shapes" width="848" height="1200" viewBox="0 0 848 1200" aria-hidden="true">
    <defs>
      <linearGradient id="header-fill" x1="0" y1="0" x2="1" y2="1">
        <stop offset="0" stop-color="#1f45a0"/>
        <stop offset="1" stop-color="#142f78"/>
      </linearGradient>
      <linearGradient id="venue-fill" x1="0" y1="0" x2="1" y2="0">
        <stop offset="0" stop-color="#66963a"/>
        <stop offset="1" stop-color="#8cb83f"/>
      </linearGradient>
    </defs>
    <ellipse class="header-band" cx="300" cy="-120" rx="470" ry="385" fill="url(#header-fill)"/>
    <ellipse class="venue-band" cx="620" cy="1330" rx="430" ry="365" fill="url(#venue-fill)"/>
  </svg>

  <header class="header-brand">
    <div class="brand-mark"></div>
    <div class="brand-name">Q-TarVM</div>
    <div class="brand-rule"></div>
    <div class="brand-tagline">Institute for Talent in Vertical Markets</div>
  </header>

  <div class="photo" role="img" aria-label="Photo of a smiling woman sitting cross-legged with a laptop on her lap"></div>

  <p class="event-date">
    <span class="day">25<sup>th</sup> January</span>
    <span class="year">2019</span>
  </p>

  <h1 class="title">
    <span class="edition">4<sup>th</sup> Annual</span>
    <span class="lead">Lift Her Forward &amp; See</span>
    <span class="rise">Her Rise!</span>
  </h1>

  <p class="venue">Harbor Crest Resort and<br>Spa, San Marcos, TX</p>
</main>
</body>
</html>
```